MOSLEN Environmental needs an upgrade to its current business cards design

We need an upgrade to our current business cards design, where the MOSLEN acronym is included, as possible and not being overloaded.
MOSLEN Environmental is an Environmental Consultancy Firm based in Sydney.
We would like to see creative designs different from the standard type of business cards (for example, rounded edges, different to standard size of common business cards.

Target Market(s)

industrial companies (oil & gas, petrochemical, mining, insolvency, finance and manufacturing), developers, architect firms, law firms.

Industry/Entity Type

Business

Contact Information for Business Card

logos (brand and acronym), if they don't appear overloaded.
name
role
name of company (MOSLEN Environmental),
address (Level 3, Suite 3C, 47-49 Dorrigan Lane, Wexmoor, NSW, 2188) landline (02 7314 2986)
mobile (staff member)
email (staff member) and
website (www.moslengreen.example).
Include: Contaminated Land, Site Remediation, Groundwater Assessment, Health and Ecological Risk Assessments, Acid Sulfate Soils, Waste Classification.

Font styles to use
Serif
Sans Serif

Requirements
Must have
• A creative design different to the standard type of business cards.
Nice to have
• Rounded edges
• Different size of business cards rather than the standard size.
Should not have
• Preferable not to use white colour background, unless it is required from a creative design proposed.
• Not an overloaded design.
• Avoid black colours

```html
<!DOCTYPE html>
<html lang="en">
<head>
<meta charset="utf-8">
<title>MOSLEN Environmental – Business Card</title>
<link rel="stylesheet" href="https://fonts.googleapis.com/css2?family=Montserrat:wght@800&family=Open+Sans:wght@400;600&display=swap">
<style>
  :root {
    --bg: #ffffff;
    --card-dark: #343434;
    --card-dark-edge: #2a2a2a;
    --green: #6ab33e;
    --green-bright: #7dc243;
    --grey: #8a8b8e;
    --text-light: #f2f2f2;
    --text-soft: #d9d9d9;
  }
  * { box-sizing: border-box; margin: 0; padding: 0; }
  html, body { width: 1200px; height: 1200px; overflow: hidden; background: var(--bg); }
  body { position: relative; font-family: "Open Sans", Arial, sans-serif; }

  .brand-mark {
    position: absolute; top: 95px; left: 0; width: 1200px;
    text-align: center;
    font-family: "Montserrat", Arial, sans-serif; font-weight: 800;
    font-size: 62px; letter-spacing: 2px; color: var(--green);
  }

  .card {
    position: absolute; left: 250px; width: 700px; height: 380px;
    border-radius: 18px; overflow: hidden;
    background: radial-gradient(circle at 55% 60%, #404040 0%, var(--card-dark) 55%, var(--card-dark-edge) 100%);
    box-shadow: 0 6px 18px rgba(0,0,0,0.18);
  }
  .card--back { top: 240px; }
  .card--front { top: 660px; }

  /* back side */
  .acronym { position: absolute; left: 46px; top: 44px; list-style: none; }
  .acronym li { display: flex; align-items: baseline; height: 48px; }
  .acronym .letter {
    width: 48px; font-family: "Montserrat", Arial, sans-serif; font-weight: 800;
    font-size: 40px; color: var(--green);
  }
  .acronym .word {
    font-family: "Montserrat", Arial, sans-serif; font-weight: 800;
    font-size: 19px; letter-spacing: 1.5px; color: var(--grey); text-transform: uppercase;
  }
  .service-panel {
    position: absolute; right: 0; top: 0; width: 290px; height: 100%;
    background: var(--green); padding: 44px 28px;
  }
  .service-panel .panel-name {
    font-family: "Montserrat", Arial, sans-serif; font-weight: 800;
    font-size: 30px; color: var(--text-light); letter-spacing: 1px; line-height: 1.1;
  }
  .service-list { margin-top: 26px; list-style: none; }
  .service-list li {
    font-size: 14.5px; color: var(--text-light); line-height: 1.95;
    padding-left: 16px; position: relative;
  }
  .service-list li::before {
    content: ""; position: absolute; left: 0; top: 12px;
    width: 6px; height: 6px; border-radius: 50%; background: var(--text-light);
  }

  /* front side */
  .front-name {
    position: absolute; left: 48px; top: 42px;
    font-family: "Montserrat", Arial, sans-serif; font-weight: 800;
    font-size: 44px; color: var(--green); letter-spacing: 1px;
  }
  .person { position: absolute; left: 52px; top: 150px; }
  .person-name { font-size: 27px; font-weight: 600; color: var(--text-light); }
  .person-role { font-size: 17px; color: var(--text-soft); margin-top: 4px; }

  .address { position: absolute; left: 52px; top: 258px; font-size: 17px; line-height: 1.42; color: var(--text-soft); font-style: normal; }
  .address .company { color: var(--green); }

  .contacts { position: absolute; left: 330px; top: 282px; list-style: none; }
  .contacts li { display: flex; align-items: center; font-size: 17px; color: var(--text-soft); height: 24.5px; }
  .contacts svg { width: 14px; height: 14px; margin-right: 14px; flex: none; }
</style>
</head>
<body>

<div class="brand-mark">MOSLEN Environmental</div>

<section class="card card--back" aria-label="Business card, back">
  <ul class="acronym">
    <li><span class="letter">M</span><span class="word">Monitoring</span></li>
    <li><span class="letter">O</span><span class="word">Of</span></li>
    <li><span class="letter">S</span><span class="word">Soil,</span></li>
    <li><span class="letter">L</span><span class="word">Land,</span></li>
    <li><span class="letter">E</span><span class="word">Ecology (and)</span></li>
    <li><span class="letter">N</span><span class="word">Nature</span></li>
  </ul>
  <div class="service-panel">
    <div class="panel-name">MOSLEN Environmental</div>
    <ul class="service-list">
      <li>Contaminated Land</li>
      <li>Site Remediation</li>
      <li>Groundwater Assessment</li>
      <li>Health &amp; Ecological Risk Assessments</li>
      <li>Acid Sulfate Soils</li>
      <li>Waste Classification</li>
    </ul>
  </div>
</section>

<section class="card card--front" aria-label="Business card, front">
  <div class="front-name">MOSLEN Environmental</div>

  <div class="person">
    <div class="person-name">Alden Corrie</div>
    <div class="person-role">Project Engineer</div>
  </div>

  <address class="address">
    <span class="company">MOSLEN Environmental</span><br>
    Level 3, Suite 3C<br>
    47-49 Dorrigan Lane<br>
    Wexmoor, NSW 2188
  </address>

  <ul class="contacts">
    <li>
      <svg viewBox="0 0 14 14" aria-hidden="true"><rect x="3" y="0.8" width="8" height="12.4" rx="1.5" fill="none" stroke="var(--green)" stroke-width="1.6"/><circle cx="7" cy="10.6" r="0.9" fill="var(--green)"/></svg>
      0412 508 337
    </li>
    <li>
      <svg viewBox="0 0 14 14" aria-hidden="true"><path d="M3 1 L5.4 1 L6.2 4.2 L4.6 5.4 C5.3 7.2 6.8 8.7 8.6 9.4 L9.8 7.8 L13 8.6 L13 11 C13 12 12.2 13 11 13 C5.5 12.6 1.4 8.5 1 3 C1 1.8 2 1 3 1 Z" fill="var(--green)"/></svg>
      02 7314 2986
    </li>
    <li>
      <svg viewBox="0 0 14 14" aria-hidden="true"><rect x="0.8" y="2.8" width="12.4" height="8.4" rx="1" fill="none" stroke="var(--green)" stroke-width="1.4"/><path d="M1 3.2 L7 7.8 L13 3.2" fill="none" stroke="var(--green)" stroke-width="1.4"/></svg>
      alden@moslengreen.example
    </li>
    <li>
      <svg viewBox="0 0 14 14" aria-hidden="true"><circle cx="7" cy="7" r="6" fill="none" stroke="var(--green)" stroke-width="1.4"/><path d="M1 7 H13 M7 1 C4.5 4 4.5 10 7 13 M7 1 C9.5 4 9.5 10 7 13" fill="none" stroke="var(--green)" stroke-width="1.1"/></svg>
      www.moslengreen.example
    </li>
  </ul>
</section>

</body>
</html>
```